Increased budget: GUI redesign: 10 year old user interface needs modern look-and-feel

UPDATE: Please DO look at more than only th eone image I attached! Almost all designs are simply reworks of that one picture. That is not what we are looking for. Check out the video to understand what the product does, and try to make something better.
We have an existing app (see https://www.vornatek.com/downloadTunePilot.php?vers=3_9_1_140964&dir=Vornatek_OEM/3_9_1_140964&name=DSP_Control_Software) which needs refreshing. See also a video here: https://vornatek-oem.com/software/ and the user manual attached here. The GUI is now 800x400 pixels, which is too small; and not scalable, which will be fixed in the future. We need a new, modern look-and-feel, and images that can be exported from the design in various sizes. The current design is attached as well as a collection of PNG files. The overall layout can stay similar, although we are open to good ideas for improvements. The design should be targeted at professional users, not end users; the product is used by audio professionals (e.g. sound engineers, loudspeaker designers). Also see our web version: https://www.vornatek.com/tunepilot/skins/1_1_2/container.html?MAC=Demo%201x2
The winner will also be asked to do a full design of the application GUI (based on the design done here), with several more windows etc, and additional payment depending on the work to be done.

Target Market(s)

Professional audio

Industry/Entity Type

Audio / Industrial

Font styles to use
Other font styles liked:
• Futura (not mandatory)

Colors

Designer to choose colors to be used in the design.

Requirements
Must have
• Modern, timeless design, not too bling bling
Nice to have
• Flat design
Should not have
• 3D, bling bling, many colours, etc

```html
<!DOCTYPE html>
<html lang="en">
<head>
<meta charset="utf-8">
<title>DSP Control Interface – Design C and D</title>
<link href="https://fonts.googleapis.com/css2?family=Open+Sans:wght@400;600;700;800&display=swap" rel="stylesheet">
<style>
:root{
  --canvas:#50565b;
  --panel:#1c1d1f;
  --topbar:#19191b;
  --column:#2a2b2d;
  --field:#1e1f21;
  --button:#56595c;
  --divider:#1f2022;
  --text:#e2e3e4;
  --muted:#a9abad;
  --placeholder:#6a6c6f;
  --accent-blue:#1f6e96;
  --accent-red:#e0253a;
  --warm:#e8b400;
  --online:#5cb23e;
}
*{box-sizing:border-box;margin:0;padding:0}
html,body{width:959px;height:1200px;overflow:hidden;background:var(--canvas)}
body{font-family:"Open Sans",Arial,sans-serif;color:var(--text)}
.stage{position:relative;width:1500px;height:1876px;transform:scale(.63933);transform-origin:0 0}
.design-title{position:absolute;left:67px;font-weight:800;font-size:24px;letter-spacing:.5px;color:#fff}
.panel{position:absolute;left:67px;width:1366px;height:768px;background:var(--panel)}
.topbar{position:absolute;left:0;top:0;width:1366px;height:48px;background:var(--topbar)}
.brand{position:absolute;left:8px;top:14px;display:flex;align-items:center;gap:4px;font-size:9px;font-weight:700;color:#e6e7e8}
.brand-mark{width:10px;height:10px;background:#2f4666}
.meta-item{position:absolute;top:0;line-height:48px;font-size:12px;color:var(--muted);white-space:nowrap}
.meta-item b{font-weight:700;color:#c9cacb}
.meta-sep{position:absolute;top:17px;width:1px;height:15px;background:#4e5154}
.header-temp{position:absolute;left:1290px;top:0;height:48px;display:flex;align-items:center;gap:6px}
.header-temp .deg{font-size:18px;color:var(--warm)}
.header-temp .unit{font-size:18px;color:#aaa;margin-left:-2px}
.band{position:absolute;top:56px;height:30px;line-height:30px;text-align:center;font-size:10px;font-weight:700;color:#f1f2f3;letter-spacing:.3px}
.band.system{left:8px;width:188px}
.band.in{left:204px;width:381px}
.band.out{left:593px;width:765px}
.design-c .band.system{background:#6ea364}
.design-c .band.in{background:#6a8a9a}
.design-c .band.out{background:#8a7fb5}
.design-d .band.system{background:#9aa46a}
.design-d .band.in{background:#6ea364}
.design-d .band.out{background:#7f92b5}
.system-column{position:absolute;left:8px;top:86px;width:188px;height:674px;background:var(--column)}
.system-column > *{position:absolute}
.sys-btn{height:35px;width:76px;line-height:35px;text-align:center;font-size:11px;color:var(--text);background:var(--button);border-radius:2px}
.sys-btn.active{background:var(--accent-blue);font-weight:700}
.small-btn{height:22px;width:76px;line-height:22px;text-align:center;font-size:11px;color:var(--text);background:var(--button);border-radius:2px}
.rule{left:0;width:188px;height:2px;background:var(--divider)}
.label{left:12px;font-size:9.5px;font-weight:600;color:#b0b2b4;text-transform:uppercase;transform:translateY(-50%)}
.status-dot{left:122px;width:9px;height:9px;border-radius:50%;background:var(--online);transform:translateY(-50%)}
.status-text{left:142px;font-size:11px;color:var(--text);transform:translateY(-50%)}
.input{left:12px;width:164px;height:32px;line-height:32px;padding-left:8px;font-size:12px;font-weight:400;background:var(--field);border-radius:2px;color:var(--placeholder)}
.input.filled{color:#f0f0f0}
.select{left:12px;width:164px;height:32px;line-height:32px;padding-left:8px;font-size:12px;background:var(--field);border-radius:2px;color:#e8e8e8}
.select i{position:absolute;right:3px;top:4px;width:27px;height:24px;background:var(--button);border-radius:2px}
.select i::after{content:"";position:absolute;left:10px;top:7px;width:5px;height:5px;border-right:1px solid #bbb;border-bottom:1px solid #bbb;transform:rotate(45deg)}
.temp-big{left:12px;font-size:31px;line-height:1;color:var(--warm)}
.temp-big sup{font-size:18px;vertical-align:top;position:relative;top:-2px}
.temp-big .unit{color:#aaa;margin-left:10px}
.strips{position:absolute;left:204px;top:86px;width:1154px;height:674px;overflow:visible}
svg text{font-family:"Open Sans",Arial,sans-serif}
.s-col{fill:var(--column)}
.s-btn{fill:var(--button)}
.s-field{fill:var(--field)}
.s-slot{fill:#141516}
.s-div{stroke:var(--divider);stroke-width:2}
.s-ticks{stroke:#5c5e61;stroke-width:5;stroke-dasharray:1 2}
.s-scale{font-size:11px;fill:#9c9ea0;text-anchor:end}
.s-ph{font-size:10px;fill:var(--placeholder)}
.s-label{font-size:9.5px;font-weight:600;fill:#b0b2b4}
.s-name{font-size:11px;fill:#e2e3e4;text-anchor:middle}
.s-fld{font-size:11px;fill:#e8e8e8}
.s-val{font-size:11px;fill:#e4e4e4}
.s-unit{font-size:10px;fill:#8a8c8e;text-anchor:end}
.s-knob{fill:#b9babc}
.s-knob-line{stroke:#7d7f81;stroke-width:1.5}
.s-meter{stroke:url(#meter-grad);stroke-width:4;stroke-dasharray:2 1}
.s-icon{fill:none;stroke:#cfd0d1;stroke-width:1.6}
.s-icon-fill{fill:#cfd0d1}
.s-link{fill:var(--button)}
.s-link.on{fill:#1f7fa8}
.s-on-blue{fill:#1f7fa8}
.s-on-red{fill:var(--accent-red)}
</style>
</head>
<body>
<div class="stage">

  <h1 class="design-title" style="top:66px">DESIGN C</h1>
  <section class="panel design-c" style="top:122px">
    <header class="topbar">
      <div class="brand"><span class="brand-mark"></span>VORNATEK</div>
      <span class="meta-item" style="left:212px"><b>IP:</b> 102.16.178.123</span>
      <span class="meta-sep" style="left:328px"></span>
      <span class="meta-item" style="left:340px"><b>MAC:</b> b8:96:74:ab:02:45</span>
      <span class="meta-sep" style="left:496px"></span>
      <span class="meta-item" style="left:509px"><b>FW:</b> 4.0.0.51134</span>
      <span class="meta-sep" style="left:622px"></span>
      <span class="meta-item" style="left:634px"><b>SETTINGS:</b> 20240423 v1 revised</span>
      <span class="meta-sep" style="left:835px"></span>
      <span class="meta-item" style="left:847px"><b>MODEL:</b> Strata 5 MK3 240RB + S V1</span>
      <span class="meta-sep" style="left:1073px"></span>
      <span class="meta-item" style="left:1085px"><b>REVISION:</b> 20231209 MD v1</span>
      <div class="header-temp">
        <svg width="12" height="22" viewBox="0 0 12 22"><rect x="3.5" y="1" width="5" height="14" rx="2.5" fill="none" stroke="#9aa35a" stroke-width="1.5"/><circle cx="6" cy="17" r="4" fill="#9aa35a"/><rect x="5" y="7" width="2" height="9" fill="#9aa35a"/></svg>
        <span class="deg">32°</span><span class="unit">C</span>
      </div>
    </header>

    <div class="band system">SYSTEM</div>
    <div class="band in">IN</div>
    <div class="band out">OUT</div>

    <div class="system-column">
      <div class="sys-btn active" style="left:12px;top:14px">MAIN</div>
      <div class="sys-btn" style="left:100px;top:14px">X-OVER</div>
      <div class="rule" style="top:62px"></div>
      <div class="label" style="top:88px">Status</div>
      <div class="status-dot" style="top:88px"></div>
      <div class="status-text" style="top:88px">Online</div>
      <div class="rule" style="top:110px"></div>
      <div class="label" style="top:135px">Local Presets</div>
      <div class="small-btn" style="left:12px;top:153px">STORE</div>
      <div class="small-btn" style="left:99px;top:153px">LOAD</div>
      <div class="rule" style="top:191px"></div>
      <div class="label" style="top:216px">Unit Presets</div>
      <div class="input" style="top:233px">Enter Name</div>
      <div class="select" style="top:273px">- Select Preset -<i></i></div>
      <div class="small-btn" style="left:12px;top:322px">STORE</div>
      <div class="small-btn" style="left:99px;top:322px">LOAD</div>
      <div class="rule" style="top:360px"></div>
      <div class="label" style="top:385px">Link</div>
      <div class="select" style="top:402px">- Select Link -<i></i></div>
      <div class="rule" style="top:449px"></div>
      <div class="label" style="top:474px">Unit Name</div>
      <div class="input filled" style="top:491px">VORNATEK VNX - 6K2</div>
    </div>

    <svg class="strips" viewBox="0 0 1154 674" aria-label="Input and output channel strips">
      <defs>
        <linearGradient id="meter-grad" gradientUnits="userSpaceOnUse" x1="0" y1="546" x2="0" y2="186">
          <stop offset="0" stop-color="#4caf3a"/><stop offset=".33" stop-color="#4caf3a"/>
          <stop offset=".34" stop-color="#e0b020"/><stop offset=".74" stop-color="#e0b020"/>
          <stop offset=".75" stop-color="#e0253a"/><stop offset="1" stop-color="#e0253a"/>
        </linearGradient>
        <g id="ico-phase"><circle class="s-icon" r="6"/><line class="s-icon" x1="-4.5" y1="4.5" x2="4.5" y2="-4.5"/></g>
        <g id="ico-spk"><path class="s-icon-fill" d="M-7,-3h3l4,-4v14l-4,-4h-3z"/><path class="s-icon" d="M2.5,-3a4,4 0 0 1 0,6M5,-5.5a7.5,7.5 0 0 1 0,11"/></g>
        <g id="ico-mute"><path fill="#fff" d="M-7,-3h3l4,-4v14l-4,-4h-3z"/><path fill="none" stroke="#fff" stroke-width="1.6" d="M2,-3.5l6,7M8,-3.5l-6,7"/></g>
        <g id="ico-link"><rect class="s-icon" x="-7" y="-3" width="8" height="6" rx="3"/><rect class="s-icon" x="-1" y="-3" width="8" height="6" rx="3"/></g>
        <g id="strip">
          <rect class="s-col" width="94" height="674"/>
          <rect class="s-btn" x="8" y="14" width="78" height="35" rx="2"/>
          <line class="s-div" x1="0" x2="94" y1="64" y2="64"/>
          <rect class="s-field" x="8" y="76" width="78" height="32" rx="2"/>
          <text class="s-ph" x="13" y="96">Ch. Name</text>
          <text class="s-scale" x="27" y="190">+24</text>
          <text class="s-scale" x="27" y="220">+18</text>
          <text class="s-scale" x="27" y="250">+12</text>
          <text class="s-scale" x="27" y="280">+6</text>
          <text class="s-scale" x="27" y="310">0</text>
          <text class="s-scale" x="27" y="340">-6</text>
          <text class="s-scale" x="27" y="370">-12</text>
          <text class="s-scale" x="27" y="400">-18</text>
          <text class="s-scale" x="27" y="430">-24</text>
          <text class="s-scale" x="27" y="460">-30</text>
          <text class="s-scale" x="27" y="490">-36</text>
          <text class="s-scale" x="27" y="520">-42</text>
          <text class="s-scale" x="27" y="550">-48</text>
          <line class="s-ticks" x1="35" x2="35" y1="186" y2="548"/>
          <rect class="s-slot" x="51" y="186" width="6" height="362"/>
          <rect class="s-slot" x="68" y="186" width="5" height="362"/>
          <rect class="s-slot" x="76" y="186" width="5" height="362"/>
          <line class="s-div" x1="0" x2="94" y1="573" y2="573"/>
          <rect class="s-field" x="8" y="596" width="78" height="28" rx="2"/>
          <text class="s-unit" x="80" y="614">dB</text>
          <rect class="s-btn" x="8" y="637" width="34" height="23" rx="2"/>
          <rect class="s-btn" x="52" y="637" width="34" height="23" rx="2"/>
          <use href="#ico-phase" x="25" y="648"/>
          <use href="#ico-spk" x="69" y="648"/>
        </g>
        <g id="src-field">
          <text class="s-label" x="8" y="127">SOURCE</text>
          <rect class="s-field" x="8" y="135" width="78" height="30" rx="2"/>
          <rect class="s-btn" x="56" y="138" width="27" height="24" rx="2"/>
          <path d="M66,148l3.5,3.5l3.5,-3.5" fill="none" stroke="#bbb" stroke-width="1"/>
        </g>
        <g id="off-field">
          <text class="s-label" x="8" y="127">OFFSET</text>
          <rect class="s-field" x="8" y="135" width="78" height="30" rx="2"/>
          <text class="s-ph" x="13" y="154">Offset</text>
        </g>
      </defs>

      <g id="channel-strips">
        <g transform="translate(0,0)"><use href="#strip"/><use href="#src-field"/>
          <text class="s-name" x="47" y="35">IN 1</text><text class="s-fld" x="13" y="154">IN - 1</text>
          <line class="s-meter" x1="70.5" y1="546" x2="70.5" y2="308"/><line class="s-meter" x1="78.5" y1="546" x2="78.5" y2="445"/>
          <rect class="s-knob" x="45" y="347" width="18" height="24" rx="2"/><line class="s-knob-line" x1="45" x2="63" y1="359" y2="359"/>
          <text class="s-val" x="14" y="614">-12.2</text></g>
        <g transform="translate(95,0)"><use href="#strip"/><use href="#src-field"/>
          <text class="s-name" x="47" y="35">IN 2</text><text class="s-fld" x="13" y="154">IN - 2</text>
          <line class="s-meter" x1="70.5" y1="546" x2="70.5" y2="284"/><line class="s-meter" x1="78.5" y1="546" x2="78.5" y2="386"/>
          <rect class="s-knob" x="45" y="395" width="18" height="24" rx="2"/><line class="s-knob-line" x1="45" x2="63" y1="407" y2="407"/>
          <text class="s-val" x="14" y="614">-24.6</text></g>
        <g transform="translate(192,0)"><use href="#strip"/><use href="#src-field"/>
          <text class="s-name" x="47" y="35">IN 3</text><text class="s-fld" x="13" y="154">IN - 3</text>
          <line class="s-meter" x1="70.5" y1="546" x2="70.5" y2="298"/><line class="s-meter" x1="78.5" y1="546" x2="78.5" y2="348"/>
          <rect class="s-knob" x="45" y="311" width="18" height="24" rx="2"/><line class="s-knob-line" x1="45" x2="63" y1="323" y2="323"/>
          <text class="s-val" x="14" y="614">-6.4</text></g>
        <g transform="translate(286,0)"><use href="#strip"/><use href="#src-field"/>
          <text class="s-name" x="47" y="35">IN 4</text><text class="s-fld" x="13" y="154">IN - 4</text>
          <line class="s-meter" x1="70.5" y1="546" x2="70.5" y2="237"/><line class="s-meter" x1="78.5" y1="546" x2="78.5" y2="410"/>
          <rect class="s-knob" x="45" y="441" width="18" height="24" rx="2"/><line class="s-knob-line" x1="45" x2="63" y1="453" y2="453"/>
          <text class="s-val" x="14" y="614">-30.0</text>
          <rect class="s-on-blue" x="8" y="637" width="34" height="23" rx="2"/><use href="#ico-phase" x="25" y="648"/></g>

        <g transform="translate(389,0)"><use href="#strip"/><use href="#off-field"/>
          <text class="s-name" x="47" y="35">OUT 1</text>
          <line class="s-meter" x1="70.5" y1="546" x2="70.5" y2="437"/><line class="s-meter" x1="78.5" y1="546" x2="78.5" y2="460"/>
          <rect class="s-knob" x="45" y="368" width="18" height="24" rx="2"/><line class="s-knob-line" x1="45" x2="63" y1="380" y2="380"/>
          <text class="s-val" x="14" y="614">-18.5</text></g>
        <g transform="translate(484,0)"><use href="#strip"/><use href="#off-field"/>
          <text class="s-name" x="47" y="35">OUT 2</text>
          <line class="s-meter" x1="70.5" y1="546" x2="70.5" y2="542"/><line class="s-meter" x1="78.5" y1="546" x2="78.5" y2="542"/>
          <rect class="s-knob" x="45" y="266" width="18" height="24" rx="2"/><line class="s-knob-line" x1="45" x2="63" y1="278" y2="278"/>
          <text class="s-val" x="14" y="614">+0.9</text>
          <rect class="s-on-red" x="52" y="637" width="34" height="23" rx="2"/><use href="#ico-mute" x="69" y="648"/></g>
        <g transform="translate(581,0)"><use href="#strip"/><use href="#off-field"/>
          <text class="s-name" x="47" y="35">OUT 3</text>
          <line class="s-meter" x1="70.5" y1="546" x2="70.5" y2="297"/><line class="s-meter" x1="78.5" y1="546" x2="78.5" y2="349"/>
          <rect class="s-knob" x="45" y="377" width="18" height="24" rx="2"/><line class="s-knob-line" x1="45" x2="63" y1="389" y2="389"/>
          <text class="s-val" x="14" y="614">-18.2</text></g>
        <g transform="translate(676,0)"><use href="#strip"/><use href="#off-field"/>
          <text class="s-name" x="47" y="35">OUT 4</text>
          <line class="s-meter" x1="70.5" y1="546" x2="70.5" y2="542"/><line class="s-meter" x1="78.5" y1="546" x2="78.5" y2="542"/>
          <rect class="s-knob" x="45" y="479" width="18" height="24" rx="2"/><line class="s-knob-line" x1="45" x2="63" y1="491" y2="491"/>
          <text class="s-val" x="14" y="614">-42.8</text>
          <rect class="s-on-red" x="52" y="637" width="34" height="23" rx="2"/><use href="#ico-mute" x="69" y="648"/></g>
        <g transform="translate(773,0)"><use href="#strip"/><use href="#off-field"/>
          <text class="s-name" x="47" y="35">OUT 5</text>
          <line class="s-meter" x1="70.5" y1="546" x2="70.5" y2="469"/><line class="s-meter" x1="78.5" y1="546" x2="78.5" y2="492"/>
          <rect class="s-knob" x="45" y="530" width="18" height="24" rx="2"/><line class="s-knob-line" x1="45" x2="63" y1="542" y2="542"/>
          <text class="s-val" x="14" y="614">-48.0</text></g>
        <g transform="translate(868,0)"><use href="#strip"/><use href="#off-field"/>
          <text class="s-name" x="47" y="35">OUT 6</text>
          <line class="s-meter" x1="70.5" y1="546" x2="70.5" y2="504"/><line class="s-meter" x1="78.5" y1="546" x2="78.5" y2="445"/>
          <rect class="s-knob" x="45" y="372" width="18" height="24" rx="2"/><line class="s-knob-line" x1="45" x2="63" y1="384" y2="384"/>
          <text class="s-val" x="14" y="614">-18.4</text></g>
        <g transform="translate(965,0)"><use href="#strip"/><use href="#off-field"/>
          <text class="s-name" x="47" y="35">OUT 7</text>
          <line class="s-meter" x1="70.5" y1="546" x2="70.5" y2="420"/><line class="s-meter" x1="78.5" y1="546" x2="78.5" y2="450"/>
          <rect class="s-knob" x="45" y="410" width="18" height="24" rx="2"/><line class="s-knob-line" x1="45" x2="63" y1="422" y2="422"/>
          <text class="s-val" x="14" y="614">-24.1</text></g>
        <g transform="translate(1060,0)"><use href="#strip"/><use href="#off-field"/>
          <text class="s-name" x="47" y="35">OUT 8</text>
          <line class="s-meter" x1="70.5" y1="546" x2="70.5" y2="302"/><line class="s-meter" x1="78.5" y1="546" x2="78.5" y2="347"/>
          <rect class="s-knob" x="45" y="293" width="18" height="24" rx="2"/><line class="s-knob-line" x1="45" x2="63" y1="305" y2="305"/>
          <text class="s-val" x="14" y="614">0.0</text></g>

        <g class="link-buttons">
          <rect class="s-link on" x="80" y="564" width="30" height="17" rx="3"/><use href="#ico-link" x="95" y="572.5"/>
          <rect class="s-link" x="272" y="564" width="30" height="17" rx="3"/><use href="#ico-link" x="287" y="572.5"/>
          <rect class="s-link" x="469" y="564" width="30" height="17" rx="3"/><use href="#ico-link" x="484" y="572.5"/>
          <rect class="s-link on" x="661" y="564" width="30" height="17" rx="3"/><use href="#ico-link" x="676" y="572.5"/>
          <rect class="s-link" x="853" y="564" width="30" height="17" rx="3"/><use href="#ico-link" x="868" y="572.5"/>
          <rect class="s-link" x="1045" y="564" width="30" height="17" rx="3"/><use href="#ico-link" x="1060" y="572.5"/>
        </g>
      </g>
    </svg>
  </section>

  <h1 class="design-title" style="top:941px">DESIGN D</h1>
  <section class="panel design-d" style="top:997px">
    <header class="topbar">
      <div class="brand"><span class="brand-mark"></span>VORNATEK</div>
      <span class="meta-item" style="left:204px"><b>IP:</b> 102.16.178.123</span>
      <span class="meta-sep" style="left:320px"></span>
      <span class="meta-item" style="left:332px"><b>MAC:</b> b8:96:74:ab:02:45</span>
      <span class="meta-sep" style="left:488px"></span>
      <span class="meta-item" style="left:501px"><b>FW:</b> 4.0.0.51134</span>
      <span class="meta-sep" style="left:614px"></span>
      <span class="meta-item" style="left:626px"><b>SETTINGS:</b> 20240423 v1 revised</span>
      <span class="meta-sep" style="left:827px"></span>
      <span class="meta-item" style="left:839px"><b>MODEL:</b> Strata 5 MK3 240RB + S V1</span>
      <span class="meta-sep" style="left:1065px"></span>
      <span class="meta-item" style="left:1077px"><b>REVISION:</b> 20231209 MD v1</span>
    </header>

    <div class="band system">SYSTEM</div>
    <div class="band in">IN</div>
    <div class="band out">OUT</div>

    <div class="system-column">
      <div class="sys-btn active" style="left:12px;top:14px">MAIN</div>
      <div class="sys-btn" style="left:100px;top:14px">X-OVER</div>
      <div class="rule" style="top:62px"></div>
      <div class="label" style="top:88px">Status</div>
      <div class="status-dot" style="top:88px"></div>
      <div class="status-text" style="top:88px">Online</div>
      <div class="rule" style="top:110px"></div>
      <div class="label" style="top:135px">Local Presets</div>
      <div class="small-btn" style="left:12px;top:153px">STORE</div>
      <div class="small-btn" style="left:99px;top:153px">LOAD</div>
      <div class="rule" style="top:191px"></div>
      <div class="label" style="top:216px">Unit Presets</div>
      <div class="input" style="top:233px">Enter Name</div>
      <div class="select" style="top:273px">- Select Preset -<i></i></div>
      <div class="small-btn" style="left:12px;top:322px">STORE</div>
      <div class="small-btn" style="left:99px;top:322px">LOAD</div>
      <div class="rule" style="top:360px"></div>
      <div class="label" style="top:385px">Link</div>
      <div class="select" style="top:402px">- Select Link -<i></i></div>
      <div class="rule" style="top:449px"></div>
      <div class="label" style="top:474px">Unit Name</div>
      <div class="input filled" style="top:491px">VORNATEK VNX - 6K2</div>
      <div class="rule" style="top:538px;height:6px;background:var(--panel)"></div>
      <div class="label" style="top:566px">Temperature</div>
      <div class="temp-big" style="top:580px">32<sup>°</sup><span class="unit">C</span></div>
      <svg style="left:166px;top:582px" width="12" height="24" viewBox="0 0 12 24"><rect x="3.5" y="1" width="5" height="15" rx="2.5" fill="none" stroke="#9aa35a" stroke-width="1.5"/><circle cx="6" cy="18.5" r="4.5" fill="#9aa35a"/><rect x="5" y="7" width="2" height="10" fill="#9aa35a"/></svg>
    </div>

    <svg class="strips" viewBox="0 0 1154 674" aria-label="Input and output channel strips">
      <use href="#channel-strips"/>
    </svg>
  </section>

</div>
</body>
</html>
```